THE VELVET MOTHS DANCE CONCERT

Hello again! We need a Front Cover for our Dance Showcase Program. Our theme is year is "LEGENDS" .
We are paying Tribute to the Musical Legends through the years. TOBIN, DARRELL HUTTON, QUILLO, ZENA BOLT etc.
It should include:
1. our Name and Logo (three girls) , which we will provide.
2. Colorful and Bright, Flashy SUPERSTAR feel to it!
3. Size for Print is 8.25 by 10.75 (front page of a magazine type booklet)
4.It should Say somewhere:
" The Velvet Moths Dance Factory presents... "
LEGENDS
5. include "2023 Annual Showcase"
6. Include our website address somewhere : www.VMKSstudios.example
7: include " Follow us @VMKS (Snapvista Logo)
you have been working with us for a few years now. Thank you for sharing your gifts and art!
Music Lovers
Entertainment

```html
<!DOCTYPE html>
<html lang="en">
<head>
<meta charset="utf-8">
<title>Legends – 2023 Annual Showcase Program Cover</title>
<link rel="stylesheet" href="https://fonts.googleapis.com/css2?family=Montserrat:wght@600;700;800&family=Lobster&display=swap">
<style>
  :root {
    --page-bg: #e9e9e9;
    --stage-dark: #1c0f08;
    --stage-mid: #4a2c14;
    --floor-light: #b98143;
    --floor-dark: #6e4421;
    --gold: #ffd000;
    --gold-deep: #f2b800;
    --white: #ffffff;
    --cream: #fff4c4;
    --flame: #e0452a;
    --magenta: #8e2a5c;
  }
  html, body {
    margin: 0;
    width: 1200px;
    height: 1200px;
    overflow: hidden;
    background: var(--page-bg);
  }
  .cover {
    position: absolute;
    left: 227px;
    top: 113px;
    width: 746px;
    height: 973px;
    overflow: hidden;
    font-family: "Montserrat", sans-serif;
  }
  .cover-art {
    position: absolute;
    inset: 0;
    width: 746px;
    height: 973px;
    display: block;
  }
  .brand-name {
    position: absolute;
    left: 20px;
    top: 172px;
    width: 190px;
    margin: 0;
    text-align: center;
    font-weight: 700;
    font-size: 20px;
    line-height: 1.3;
    color: var(--white);
    letter-spacing: 0.5px;
  }
  .presents {
    position: absolute;
    left: 31px;
    top: 344px;
    margin: 0;
    font-weight: 800;
    font-size: 25px;
    line-height: 38px;
    color: var(--white);
  }
  .presents .accent,
  .showcase .accent { color: var(--gold); }
  .showcase {
    position: absolute;
    left: 31px;
    top: 549px;
    margin: 0;
    font-weight: 800;
    font-size: 25px;
    line-height: 34px;
    color: var(--white);
  }
  .title {
    position: absolute;
    left: 0;
    width: 758px;
    top: 770px;
    margin: 0;
    text-align: center;
    font-family: "Lobster", cursive;
    font-weight: 400;
    font-size: 132px;
    line-height: 1;
    background: linear-gradient(90deg, var(--white) 20%, var(--cream) 55%, #ffe66a 100%);
    -webkit-background-clip: text;
    background-clip: text;
    color: transparent;
  }
  .title-rule {
    position: absolute;
    top: 904px;
    height: 2px;
    background: var(--white);
  }
  .title-rule.left { left: 145px; width: 144px; }
  .title-rule.right { left: 348px; width: 254px; }
  .contact-bar {
    position: absolute;
    left: 0;
    right: 0;
    top: 936px;
    display: flex;
    justify-content: center;
    align-items: center;
    gap: 10px;
    font-weight: 600;
    font-size: 14px;
    color: var(--white);
  }
  .contact-divider {
    width: 1px;
    height: 26px;
    background: var(--white);
    margin: 0 6px;
  }
  .globe-icon { width: 20px; height: 20px; display: block; }
</style>
</head>
<body>
<main class="cover">
  <svg class="cover-art" viewBox="0 0 746 973" xmlns="http://www.w3.org/2000/svg">
    <defs>
      <linearGradient id="stageGrad" x1="0" y1="0" x2="0" y2="1">
        <stop offset="0" stop-color="#140905"/>
        <stop offset="0.45" stop-color="#3a2210"/>
        <stop offset="0.72" stop-color="var(--stage-mid)"/>
        <stop offset="0.76" stop-color="#2a160a"/>
        <stop offset="0.83" stop-color="var(--floor-light)"/>
        <stop offset="1" stop-color="var(--floor-dark)"/>
      </linearGradient>
      <linearGradient id="starGrad" x1="0" y1="0" x2="1" y2="1">
        <stop offset="0" stop-color="#ffd65c"/>
        <stop offset="0.25" stop-color="#ff7a2a"/>
        <stop offset="0.6" stop-color="var(--flame)"/>
        <stop offset="1" stop-color="var(--magenta)"/>
      </linearGradient>
      <linearGradient id="hexTopGrad" x1="0" y1="0" x2="0" y2="1">
        <stop offset="0" stop-color="#6d4e8a"/>
        <stop offset="1" stop-color="#1d1a22"/>
      </linearGradient>
      <linearGradient id="hexMidGrad" x1="0" y1="0" x2="1" y2="1">
        <stop offset="0" stop-color="#6d6a44"/>
        <stop offset="1" stop-color="#2c2a1c"/>
      </linearGradient>
      <linearGradient id="hexLowGrad" x1="0" y1="0" x2="1" y2="1">
        <stop offset="0" stop-color="#3b2a6a"/>
        <stop offset="1" stop-color="#b88be0"/>
      </linearGradient>
      <linearGradient id="goldGrad" x1="0" y1="0" x2="1" y2="1">
        <stop offset="0" stop-color="var(--gold-deep)"/>
        <stop offset="1" stop-color="var(--gold)"/>
      </linearGradient>
    </defs>

    <rect class="stage-backdrop" x="0" y="0" width="746" height="973" fill="url(#stageGrad)" role="img" aria-label="Theatre stage with glittering lights and a wooden floor"/>

    <polygon class="star-photo" points="335,0 746,0 746,509 441,664 335,664" fill="url(#starGrad)" role="img" aria-label="Photo of ZENA BOLT performing on stage in front of flames"/>

    <polygon class="gold-band" points="334,0 520,0 441,58" fill="url(#goldGrad)"/>
    <polygon class="gold-wedge" points="652,455 746,402 746,508" fill="url(#goldGrad)"/>
    <polygon class="gold-wedge" points="227,660 332,725 227,771" fill="url(#goldGrad)"/>

    <g class="legend-hexes" stroke="var(--gold)" stroke-width="6" stroke-linejoin="miter">
      <polygon points="334,-7 441,53 441,179 334,238 227,179 227,53" fill="url(#hexTopGrad)" role="img" aria-label="Photo of DARRELL HUTTON performing in a military-style jacket"/>
      <polygon points="334,242 441,302 441,417 334,477 227,417 227,302" fill="url(#hexMidGrad)" role="img" aria-label="Photo of TOBIN singing in a gold sequin jacket"/>
      <polygon points="334,483 441,543 441,664 334,725 227,664 227,543" fill="url(#hexLowGrad)" role="img" aria-label="Photo of QUILLO playing guitar in a white suit"/>
    </g>
  </svg>

  <p class="brand-name">The Velvet Moths<br>Dance Factory</p>

  <h2 class="presents">
    <span class="accent">The Velvet<br>Moths Dance</span><br>
    Factory<br>
    presents... "
  </h2>

  <h2 class="showcase">
    <span class="accent">2023</span><br>
    Annual<br>
    Showcase
  </h2>

  <h1 class="title">Legends</h1>
  <div class="title-rule left"></div>
  <div class="title-rule right"></div>

  <footer class="contact-bar">
    <span class="contact-social">Follow us @VMKS</span>
    <span class="contact-network">Snapvista</span>
    <span class="contact-divider"></span>
    <svg class="globe-icon" viewBox="0 0 20 20" fill="none" stroke="#ffffff" stroke-width="1.3">
      <circle cx="10" cy="10" r="8.5"/>
      <ellipse cx="10" cy="10" rx="3.8" ry="8.5"/>
      <line x1="1.5" y1="10" x2="18.5" y2="10"/>
      <path d="M3 5.5 H17 M3 14.5 H17"/>
    </svg>
    <span class="contact-web">www.VMKSstudios.example</span>
  </footer>
</main>
</body>
</html>
```